Ridgeway Harbor Real Estate Business Cards

Looking to create a template for the agents in my office. The images below are an example of our current card, logos, and tagline. The requirements are:
1. Needs to include photo of agent
2. Needs to include Logo
3. Needs to include tag line. (current card doesn't include tagline.)
4. Needs to include phone, address, email, website and social media logos i.e. Find me at "f", "twitter (logo)" etc.
5. Need front and back design.
6. I don't want the old style safe style of business card. I want it to stand out in a stack of cards.
7. Do not make it look anything like what i currently have. This needs to be all new.
Thank you for your time.
Industry/Entity Type
Real Estate Agent
Contact Information for Business Card
I need name, address, email, website (www.brindlecoveopenhouse.example) social media logos
Requirements
Must have
- 1. Needs to include photo of agent
- 2. Needs to include Logo
- 3. Needs to include tag line. (current card doesn't include tagline.)
- 4. Needs to include phone, address, email, website and social media logos i.e. Find me at "f", "twitter (logo)" etc.
- 5. Need front and back design.
- 6. I don't want the old style safe style of business card. I want it to stand out in a stack of cards.
- 7. Do not make it look anything like what i currently have. This needs to be all new.
Should not have
- Not boring or plain.

```html
<!DOCTYPE html>
<html lang="en">
<head>
<meta charset="utf-8">
<title>Ridgeway Harbor Real Estate – Business Cards</title>
<link rel="stylesheet" href="https://fonts.googleapis.com/css2?family=Montserrat:wght@800&family=Open+Sans:wght@400&family=Questrial&display=swap">
<style>
  :root {
    --backdrop: #5b3f2c;
    --card-white: #ffffff;
    --band-dark: #3c3c3c;
    --band-light: #5a5a5a;
    --back-card: #353535;
    --back-logo: #4a4a4a;
    --back-tagline: #454545;
    --brand-red: #d3202e;
    --ink: #1e1e1e;
    --suit: #3a3b3d;
  }
  * { box-sizing: border-box; margin: 0; padding: 0; }
  html, body { width: 1200px; height: 1000px; overflow: hidden; }
  body { background: var(--backdrop); position: relative; font-family: "Open Sans", sans-serif; }

  .card { position: absolute; left: 266px; width: 666px; height: 397px; overflow: hidden; box-shadow: 0 6px 14px rgba(0,0,0,.35); }
  .card--front { top: 74px; background: var(--card-white); }
  .card--back { top: 533px; background: var(--back-card); }

  .city-band {
    position: absolute; left: 0; top: 44px; width: 100%; height: 160px;
    background: linear-gradient(90deg, var(--band-dark) 0%, var(--band-dark) 45%, var(--band-light) 100%);
  }
  .agent-photo {
    position: absolute; left: 346px; top: 21px; width: 290px; height: 376px;
    background: linear-gradient(180deg, #8d8f93 0%, #6b6d70 35%, var(--suit) 60%, #2c2d2f 100%);
  }

  .brand-name {
    position: absolute; left: 32px; top: 86px; width: 300px;
    font-family: "Montserrat", sans-serif; font-weight: 800; color: var(--card-white);
    font-size: 27px; line-height: 1.05; letter-spacing: -0.5px; text-transform: uppercase;
  }
  .tagline {
    position: absolute; left: 32px; top: 148px;
    font-family: "Questrial", sans-serif; font-size: 17px; color: var(--card-white); white-space: nowrap;
  }

  .contact-list { position: absolute; left: 32px; top: 227px; list-style: none; font-size: 15.5px; color: var(--ink); }
  .contact-list li { display: flex; align-items: center; height: 22.5px; white-space: nowrap; }
  .contact-list li.address { margin-top: 5px; }
  .contact-list svg { width: 13px; height: 13px; margin-right: 9px; flex: none; }
  .social-dots { display: flex; gap: 4px; margin-right: 8px; }
  .social-dots span { width: 9px; height: 9px; border-radius: 50%; background: var(--brand-red); }

  .back-brand {
    position: absolute; left: 0; width: 100%; top: 144px; text-align: center;
    font-family: "Montserrat", sans-serif; font-weight: 800; color: var(--back-logo);
    font-size: 36px; line-height: 1.05; text-transform: uppercase; letter-spacing: -0.5px;
  }
  .back-tagline {
    position: absolute; left: 0; width: 100%; top: 232px; text-align: center;
    font-family: "Questrial", sans-serif; font-size: 22px; color: var(--back-tagline);
  }
</style>
</head>
<body>

<section class="card card--front">
  <div class="city-band" role="img" aria-label="Greyscale city skyline photograph"></div>
  <div class="agent-photo" role="img" aria-label="Photo of the agent in a dark suit with arms crossed"></div>

  <h1 class="brand-name">Ridgeway Harbor<br>Real Estate</h1>
  <p class="tagline">Find Home. Live Well. Settle In.</p>

  <ul class="contact-list">
    <li><span class="social-dots"><span></span><span></span><span></span></span>@ridgewayharbor</li>
    <li>
      <svg viewBox="0 0 14 14"><path fill="#d3202e" d="M1 5c0-2 2-3 6-3s6 1 6 3l-3 1-1-2H5L4 6zM3 7h8l1 5H2z"/></svg>
      + 000 000 0000
    </li>
    <li>
      <svg viewBox="0 0 14 14"><path fill="#d3202e" d="M4 1h6v3H4zM1 5h12v6h-2V9H3v2H1zM4 10h6v3H4z"/></svg>
      + 000 000 0000
    </li>
    <li>
      <svg viewBox="0 0 14 14"><path fill="#d3202e" d="M1 3h12v1L7 8 1 4zM1 5.5l6 4 6-4V11H1z"/></svg>
      info@brindlecoveopenhouse.example
    </li>
    <li>
      <svg viewBox="0 0 14 14"><circle cx="7" cy="7" r="6" fill="#d3202e"/><path d="M1 7h12M7 1c-3 3-3 9 0 12M7 1c3 3 3 9 0 12" stroke="#fff" stroke-width="1" fill="none"/></svg>
      www.brindlecoveopenhouse.example
    </li>
    <li class="address">18 North Alder Ln Westbrook, MD 2170</li>
  </ul>
</section>

<section class="card card--back">
  <h2 class="back-brand">Ridgeway Harbor<br>Real Estate</h2>
  <p class="back-tagline">Find Home. Live Well. Settle In.</p>
</section>

</body>
</html>
```